We are a music event management company based out of Syracuse, NY but we do business in multiple areas like the mid-west and Florida.

Our primary events revolve around the Electronic Dance Music scene. (acts like Brinmoor, Nordic Loft Syndicate, Dorian Pell)

We would like a clean cut business card with Voltaramble written on the back. In Voltaramble we would like the u to be shaped like a sixteenth note. The colors green and silver would be nice to see somehow but not necessary. Feel free to play around with it and have fun because that's what our business is about, Having Fun!

Some similar examples for reference would be the Neon Orchard or Glowing Tulip Jamboree website.

Our goal is to provide people with an experience, not just a concert. There is a difference.

Reason: Needed more time to decide.

Industry/Entity Type

Events

```html
<!DOCTYPE html>
<html lang="en">
<head>
<meta charset="utf-8">
<title>Voltaramble Business Card</title>
<link href="https://fonts.googleapis.com/css2?family=Raleway:wght@300;400&display=swap" rel="stylesheet">
<style>
  :root {
    --page: #ffffff;
    --card: #dcdcdc;
    --ink: #3a3a3a;
    --ink-soft: #6e6e6e;
    --ink-dark: #1e1e1e;
    --icon: #9a9a9a;
    --accent-red: #e8231f;
    --tick-red: #ef3b1a;
  }
  * { margin: 0; padding: 0; box-sizing: border-box; }
  html, body {
    width: 1200px; height: 1000px; overflow: hidden;
    background: var(--page);
    font-family: "Raleway", sans-serif;
  }
  .card {
    position: absolute; left: 200px; width: 800px; height: 456px;
    background: var(--card);
    background-image: radial-gradient(rgba(0,0,0,0.035) 1px, transparent 1px);
    background-size: 3px 3px;
  }
  .card--front { top: 31px; }
  .card--back { top: 511px; }

  .holder-name {
    position: absolute; left: 39px; top: 38px;
    font-size: 29px; font-weight: 400; color: var(--ink);
  }
  .holder-title {
    position: absolute; left: 40px; top: 70px;
    font-size: 16px; font-weight: 400; color: var(--ink-soft);
  }

  .hero-art {
    position: absolute; left: 168px; top: 78px; width: 464px; height: 316px;
    border-radius: 40% / 50%;
    background: radial-gradient(ellipse at center, rgba(110,210,40,0.5) 0%, rgba(150,220,60,0.3) 50%, rgba(220,220,220,0) 72%);
  }
  .hero-wordmark {
    position: absolute; left: 0; width: 800px; top: 213px;
    text-align: center;
    font-size: 32px; font-weight: 400; letter-spacing: 1px; color: var(--ink-dark);
  }

  .contact {
    position: absolute; left: 34px; top: 352px;
    list-style: none;
  }
  .contact__item {
    display: flex; align-items: center; height: 25.5px;
    font-size: 18px; color: var(--ink); font-weight: 400;
  }
  .contact__icon { width: 26px; height: 22px; margin-right: 10px; fill: var(--icon); }

  .tagline {
    position: absolute; left: 529px; top: 391px;
    font-size: 22px; color: var(--accent-red); font-weight: 400;
  }

  .signal-bar { position: absolute; top: 230px; height: 16px; }
  .signal-bar--left {
    left: 0; width: 90px;
    background: linear-gradient(90deg, #8fdc2a, #d8e020 50%, #f0a020 80%, #f06a1a);
  }
  .signal-bar--right {
    right: 0; width: 88px; top: 227px;
    background: linear-gradient(90deg, #f05a1a, #f0a020 35%, #d8e020 65%, #8fdc2a);
  }
  .tick { position: absolute; width: 4px; height: 16px; background: var(--tick-red); }
  .tick--left { left: 110px; top: 231px; }
  .tick--right { left: 686px; top: 228px; }

  .back-wordmark {
    position: absolute; left: 141px; top: 208px;
    font-size: 40px; font-weight: 400; letter-spacing: 0.5px; color: var(--ink-dark);
  }
  .back-web {
    position: absolute; left: 462px; top: 229px;
    font-size: 18px; color: var(--ink-soft); font-weight: 400;
  }
</style>
</head>
<body>

<section class="card card--front">
  <h1 class="holder-name">Marcus T Delvane</h1>
  <p class="holder-title">CEO</p>

  <div class="hero-art" role="img" aria-label="Colourful equalizer bars with rainbow paint splatter radiating from the centre"></div>
  <div class="hero-wordmark">VOLTARAMBLE</div>

  <ul class="contact">
    <li class="contact__item">
      <svg class="contact__icon" viewBox="0 0 26 22"><path d="M7 1c1.5 0 2.5 3 2.5 4.5S7.5 7 7.5 8.5s2.5 6 4 7.5 2.5-.5 3.5-.5 3 1.5 3 3-1.5 2.5-3 2.5C10 21 4 13 4 6 4 3 5.5 1 7 1z"/></svg>
      315-555-0142
    </li>
    <li class="contact__item">
      <svg class="contact__icon" viewBox="0 0 26 22"><path d="M1 4h24v14H1z"/><path d="M1 4l12 8 12-8" fill="none" stroke="#dcdcdc" stroke-width="1.6"/></svg>
      marcus@voltarambleny.com
    </li>
    <li class="contact__item">
      <svg class="contact__icon" viewBox="0 0 26 22"><circle cx="13" cy="11" r="3.2"/><path d="M8 6a7 7 0 0 0 0 10M18 6a7 7 0 0 1 0 10M4.5 3a12 12 0 0 0 0 16M21.5 3a12 12 0 0 1 0 16" fill="none" stroke="#9a9a9a" stroke-width="1.8"/></svg>
      www.voltarambleny.com
    </li>
  </ul>

  <p class="tagline">It’s an Experience</p>
</section>

<section class="card card--back">
  <div class="signal-bar signal-bar--left"></div>
  <div class="tick tick--left"></div>
  <div class="back-wordmark">VOLTARAMBLE</div>
  <div class="back-web">www.voltarambleny.com</div>
  <div class="tick tick--right"></div>
  <div class="signal-bar signal-bar--right"></div>
</section>

</body>
</html>
```